Professional, elegant brochure for funeral home

We have a funeral home. We would like a 2 sided brochure. On one side will be 3 columns for our cremation options and on the other side would be 2-3 columns of our burial options. Would like to print it and also will be putting it on our website at www.Varnelhaven.com

Use as examples

https://www.brimtolgrace.com/pricing-and-resources/online-cremation-package-options

https://pelladinechapel.com/wp-content/uploads/Cremation-with-Ceremony-Plans.pdf

We only need a simple 1page (front and back brochure). Once we have decided on the designer I can provide the final content to be placed on the brochure.

Target Market(s)

We are family owned business so Something soft, inviting, personable and looks professionally done.

Industry/Entity Type

Funeral Home

Requirements
Must have
• Look professional. Easy to read
Nice to have
• Softer Muted comforting colors. No bright colors.

```html
<!DOCTYPE html>
<html lang="en">
<head>
<meta charset="utf-8">
<title>Burial Options – Varnel Haven Funeral Home</title>
<link rel="stylesheet" href="https://fonts.googleapis.com/css2?family=Open+Sans:wght@400;600&family=Tinos&display=swap">
<style>
  :root {
    --page-bg: #e4e6e8;
    --paper: #ffffff;
    --blue: #6b9cb4;
    --blue-soft: #c3d7df;
    --olive: #a9ab7d;
    --olive-dark: #8a8b3e;
    --ink: #5b5d5f;
    --ink-dark: #3d4144;
    --shade: #ececec;
  }
  * { box-sizing: border-box; margin: 0; padding: 0; }
  html, body { width: 1200px; height: 823px; overflow: hidden; }
  body {
    background: var(--page-bg);
    font-family: "Open Sans", sans-serif;
    color: var(--ink);
  }
  .flyer {
    position: absolute;
    left: 300px; top: 23px;
    width: 600px; height: 776px;
    background: linear-gradient(to bottom, var(--paper) 0%, var(--paper) 42%, var(--blue-soft) 92%);
    box-shadow: 0 4px 14px rgba(0,0,0,.18);
    overflow: hidden;
  }
  .hero {
    position: absolute;
    left: 14px; top: 16px;
    width: 572px; height: 285px;
    background:
      radial-gradient(ellipse at 72% 30%, rgba(246,248,236,.95) 0%, rgba(200,214,170,.6) 22%, rgba(0,0,0,0) 48%),
      radial-gradient(ellipse at 85% 70%, #cdd6cf 0%, #b3c0b5 30%, rgba(0,0,0,0) 55%),
      linear-gradient(100deg, #2f4a2c 0%, #54703e 30%, #8ea468 55%, #b9c79b 75%, #8aa070 100%);
  }
  .hero-bench {
    position: absolute;
    left: 0; bottom: 0; width: 100%; height: 36px;
    background: linear-gradient(to bottom, #5f7258, #3c4d3a);
  }
  .brand-tab {
    position: absolute;
    left: 38px; top: 16px;
    width: 193px; height: 78px;
    background: var(--paper);
    border-radius: 0 0 14px 14px;
    display: flex; align-items: center; justify-content: center; gap: 8px;
  }
  .brand-mark {
    width: 12px; height: 12px; border-radius: 50%;
    background: var(--blue);
  }
  .brand-name {
    font-family: "Open Sans", sans-serif;
    font-weight: 600;
    font-size: 13px;
    line-height: 1.25;
    letter-spacing: .06em;
    color: var(--ink-dark);
    text-transform: uppercase;
  }
  .hero-copy {
    position: absolute;
    left: 38px; top: 117px;
    color: #fff;
  }
  .hero-title {
    font-family: "Tinos", serif;
    font-weight: 400;
    font-size: 40px;
    line-height: 1;
    margin-bottom: 14px;
  }
  .hero-tagline { font-size: 13px; line-height: 1.2; letter-spacing: -.01em; }
  .hero-sub { font-size: 11px; line-height: 1.5; }

  .popular-tag {
    position: absolute;
    left: 226px; top: 297px;
    width: 161px; height: 22px;
    background: var(--olive-dark);
    color: #eef0dc;
    font-size: 9px;
    text-align: center;
    line-height: 22px;
    letter-spacing: .02em;
  }
  .package {
    position: absolute;
    width: 179px;
    background: var(--paper);
    box-shadow: 0 2px 6px rgba(0,0,0,.12);
    border-radius: 8px 8px 0 0;
    overflow: hidden;
  }
  .package--traditional { left: 20px; top: 335px; height: 352px; }
  .package--popular { left: 215px; top: 318px; height: 378px; }
  .package--graveside { left: 407px; top: 335px; height: 352px; }
  .package-head { position: relative; height: 96px; }
  .package-head svg { position: absolute; left: 0; top: 0; }
  .package-title {
    position: relative;
    font-family: "Tinos", serif;
    font-size: 17px;
    line-height: 1.18;
    color: #fff;
    text-align: center;
    padding-top: 20px;
  }
  .package--popular .package-title { padding-top: 22px; }
  .package-list {
    list-style: none;
    padding: 14px 0 0 17px;
    font-size: 11.6px;
    line-height: 20.6px;
  }
  .package--popular .package-list { padding-top: 31px; padding-left: 22px; }
  .package-list li { position: relative; padding-left: 9px; }
  .package-list li::before {
    content: ""; position: absolute; left: 0; top: 9px;
    width: 3.5px; height: 3.5px; border-radius: 50%;
    background: var(--blue);
  }
  .package--popular .package-list li::before { background: var(--olive); }
  .package-list li.cont::before { display: none; }
  .package-price {
    position: absolute;
    left: 18px; bottom: 0;
    width: 141px; height: 27px;
    background: var(--blue);
    color: #fff;
    font-family: "Tinos", serif;
    font-size: 15.5px;
    text-align: center;
    line-height: 28px;
  }
  .package--popular .package-price { background: var(--olive); }

  .contact-bar {
    position: absolute;
    left: 0; top: 725px;
    width: 100%; height: 51px;
    background: var(--olive);
    color: #fff;
    font-size: 13.4px;
    display: flex; align-items: center; justify-content: center; gap: 13px;
  }
</style>
</head>
<body>
  <main class="flyer">
    <div class="hero" role="img" aria-label="Photograph of an elderly couple seen from behind, sitting close together on a park bench among soft green trees">
      <div class="hero-bench"></div>
    </div>

    <div class="brand-tab">
      <span class="brand-mark"></span>
      <span class="brand-name">Varnel Haven<br>Funeral Home</span>
    </div>

    <header class="hero-copy">
      <h1 class="hero-title">Burial Options</h1>
      <p class="hero-tagline">TRADITIONAL. PROFOUND. HEALING.</p>
      <p class="hero-sub">Design a permanent resting place for your loved one.</p>
    </header>

    <div class="popular-tag">MOST POPULAR</div>

    <section class="package package--traditional">
      <div class="package-head">
        <svg width="179" height="96" viewBox="0 0 179 96">
          <polygon points="8,70 89,96 171,70 171,76 89,100 8,76" fill="var(--shade)"/>
          <polygon points="0,0 179,0 179,66 89,93 0,66" fill="var(--blue)"/>
        </svg>
        <h2 class="package-title">Traditional Funeral<br>Ceremony</h2>
      </div>
      <ul class="package-list">
        <li>Professional Services</li>
        <li>Transfer of Deceased</li>
        <li>Care &amp; Preparation</li>
        <li>Funeral Ceremony</li>
        <li>Visitation (2 Hours)</li>
        <li>Funeral Cremation</li>
        <li class="cont">(at Venue of Choice)</li>
        <li>Graveside Ceremony</li>
        <li>Hearse</li>
        <li>Utility Vehicle</li>
      </ul>
      <div class="package-price">$6,245</div>
    </section>

    <section class="package package--popular">
      <div class="package-head">
        <svg width="178" height="96" viewBox="0 0 178 96">
          <polygon points="8,70 89,96 170,70 170,76 89,100 8,76" fill="var(--shade)"/>
          <polygon points="0,0 178,0 178,68 89,93 0,68" fill="var(--olive)"/>
        </svg>
        <h2 class="package-title">Funeral<br>Ceremony</h2>
      </div>
      <ul class="package-list">
        <li>Professional Services</li>
        <li>Transfer of Deceased</li>
        <li>Care &amp; Preparation</li>
        <li>Funeral Cremation</li>
        <li class="cont">(at Venue of Choice)</li>
        <li>Graveside Ceremony</li>
        <li>Hearse</li>
        <li>Utility Vehicle</li>
      </ul>
      <div class="package-price">$5,745</div>
    </section>

    <section class="package package--graveside">
      <div class="package-head">
        <svg width="179" height="96" viewBox="0 0 179 96">
          <polygon points="8,70 89,96 171,70 171,76 89,100 8,76" fill="var(--shade)"/>
          <polygon points="0,0 179,0 179,66 89,93 0,66" fill="var(--blue)"/>
        </svg>
        <h2 class="package-title">Traditional Graveside<br>Ceremony</h2>
      </div>
      <ul class="package-list">
        <li>Professional Services</li>
        <li>Transfer of Deceased</li>
        <li>Care &amp; Preparation</li>
        <li>Graveside Ceremony</li>
        <li>Hearse</li>
        <li>Utility Vehicle</li>
      </ul>
      <div class="package-price">$5,645</div>
    </section>

    <footer class="contact-bar">
      <span>418 Meadow Lane Fairbrook, NY 14390</span><span>|</span>
      <span>(555) 014-2268</span><span>|</span>
      <span>www.varnelhaven.com</span>
    </footer>
  </main>
</body>
</html>
```